Flyer for The Quiet Meadow Renewal Ring

I am launching my new offering in my business at an event next Sunday where I have a booth and need a flyer advertising the offering, so the flyer needs to stand out for other practitioners that will also be there on the day offering there services.
This flyer is also what I will use for marketing on social media as well as on the day of the event. See the link below to the offering
http://carolinebirchwood.com.au/quiet-meadow-renewal-ring/

Target Market(s)

Women with body image issues - age range 25 - 65
Women with issues around food such as binge eating, emotional eating, eating disorders.

Industry/Entity Type

Health And Wellness

Font styles to use
Serif
Sans Serif
Script

Colors
f9d9e8
85cae6
cee9f5
fee18a
ffffff
eea4c8

Requirements
Must have
• Colours matching my overall website at carolinebirchwood.com.au - pinks, light blue, gold, white
• Imagery similiar to my Instagram, see below https://www.instagram.com/lanternfieldcarexq/
• - soft, warm, welcoming, nurturing, safe, inviting - see image on sales page for inspiration
• contact details
Should not have
• harsh dark colours or harsh lines

```html
<!DOCTYPE html>
<html lang="en">
<head>
<meta charset="utf-8">
<title>The Quiet Meadow Renewal Ring – Flyer</title>
<link href="https://fonts.googleapis.com/css2?family=Bebas+Neue&family=Open+Sans:ital,wght@0,400;0,600;0,700;1,400&family=Tinos:ital,wght@1,700&display=swap" rel="stylesheet">
<style>
  :root{
    --pink:#ec3f86;
    --pink-soft:#eea4c8;
    --blush:#f9d9e8;
    --blue:#1fb6d0;
    --blue-soft:#85cae6;
    --ink:#1c1c1c;
    --text:#3a3a3a;
    --paper-1:#f3e6cc;
    --paper-2:#e2cfa8;
    --white:#ffffff;
  }
  *{box-sizing:border-box;margin:0;padding:0}
  html,body{width:1041px;height:1200px;overflow:hidden;background:var(--white)}
  .flyer{
    position:relative;width:1041px;height:1200px;overflow:hidden;
    font-family:"Open Sans",sans-serif;color:var(--text);
    background:linear-gradient(100deg,#fbeef4 0%,#f6d2e3 45%,#efb7d3 100%);
  }
  .hero-photo{
    position:absolute;left:0;top:430px;width:760px;height:770px;
    background:
      radial-gradient(ellipse 55% 45% at 30% 45%,rgba(236,196,190,.95),rgba(236,196,190,0) 70%),
      radial-gradient(ellipse 60% 50% at 40% 100%,rgba(74,36,30,.95),rgba(74,36,30,0) 75%),
      linear-gradient(180deg,rgba(240,205,210,0) 0%,rgba(226,176,178,.85) 35%,rgba(150,90,84,.9) 80%);
    -webkit-mask-image:linear-gradient(90deg,#000 45%,transparent 92%);
            mask-image:linear-gradient(90deg,#000 45%,transparent 92%);
  }
  .brand{position:absolute;left:34px;top:48px;width:330px;text-align:center}
  .brand-name{font-size:30px;font-weight:600;color:var(--pink);letter-spacing:.5px}
  .title{position:absolute;left:30px;top:118px;width:340px;font-family:"Bebas Neue",sans-serif;line-height:.88}
  .title span{display:block}
  .title .t1{font-size:88px;color:var(--pink)}
  .title .t2{font-size:50px;color:var(--blue);margin:6px 0 8px}
  .title .t3{font-size:118px;color:var(--pink)}
  .note{
    position:absolute;left:392px;top:44px;width:610px;height:345px;
    transform:rotate(-2.2deg);
    background:linear-gradient(135deg,var(--paper-1),var(--paper-2));
    box-shadow:0 14px 18px -10px rgba(80,40,40,.45);
    padding:88px 26px 20px;text-align:center;
    font-family:"Tinos",serif;font-style:italic;font-weight:700;font-size:14.5px;line-height:22px;color:var(--ink);
  }
  .note-photo{
    position:absolute;left:40px;top:40px;width:96px;height:96px;border-radius:50%;
    border:4px solid var(--white);
    background:radial-gradient(circle at 50% 40%,#e9b8b0,#c86f86 60%,#f2d6dc);
  }
  .note-pin{position:absolute;left:288px;top:38px}
  .content{position:absolute;right:32px;top:452px;width:640px;text-align:right}
  .intro{font-size:13.5px;font-weight:700;color:var(--ink);line-height:21px}
  .heading{font-size:21px;font-weight:700;color:var(--pink);line-height:26px;margin:16px 0 10px}
  .copy{font-size:13.5px;line-height:19px}
  .copy + .copy{margin-top:12px}
  .perks{list-style:none;font-size:13.5px;line-height:19px}
  .perks li{position:relative;padding-right:20px;margin-bottom:8px}
  .perks li::after{content:"";position:absolute;right:2px;top:7px;width:6px;height:6px;border-radius:50%;background:var(--pink)}
  .perks .wrap{display:inline-block;max-width:400px}
  .price{margin-top:14px;display:inline-block;max-width:340px}
  .cta{font-family:"Bebas Neue",sans-serif;line-height:1}
  .cta-ready{font-size:60px;color:var(--blue);margin-top:16px}
  .cta-call{font-size:32px;color:var(--pink);margin-top:4px}
  .cta-phone{font-size:50px;color:var(--pink);letter-spacing:1px}
  .contact{font-size:13.5px;font-weight:600;color:var(--pink);line-height:20px;margin-top:4px}
  .contact div{display:flex;justify-content:flex-end;align-items:center;gap:8px}
</style>
</head>
<body>
<main class="flyer">
  <div class="hero-photo" role="img" aria-label="Soft close-up photograph of a woman resting peacefully with eyes closed"></div>

  <header class="brand">
    <div class="brand-name">Caroline Birchwood</div>
  </header>

  <h1 class="title">
    <span class="t1">THE QUIET</span>
    <span class="t2">MEADOW RENEWAL</span>
    <span class="t3">RING</span>
  </h1>

  <aside class="note">
    <div class="note-photo" role="img" aria-label="Portrait of the coach sitting relaxed with a laptop"></div>
    <svg class="note-pin" width="22" height="22" viewBox="0 0 22 22" aria-hidden="true"><circle cx="11" cy="11" r="9" fill="#111"/><circle cx="8" cy="8" r="2.5" fill="#666"/></svg>
    <p>It's time to make a commitment….<br>
    It's time for YOU, to SHOW UP for YOU…..<br>
    It's time to truly let go…….and finally heal, and find the peace that you so long for…<br>
    You deserve to feel the freedom that comes with truly loving and accepting your body.<br>
    You deserve the freedom that comes with experiencing a deeper trusting<br>
    connection with your body, where you feel safe, at home.<br>
    Can you even imagine a whole day that you didn't hate your body,<br>
    you didn't fight with food, and you felt peaceful and at home with your body?<br>
    Can you love the part of you, that hates your body?<br>
    You can't heal something you hate.</p>
  </aside>

  <section class="content">
    <p class="intro">It's time to show up for YOU, consistently, every week, and do the work, once and for all.<br>
    No more games, no more half in on YOU….<br>
    You deserve better than a life contained in the mental prison of body hatred.</p>

    <h2 class="heading">Are you truly ready to make the commitment?</h2>
    <p class="copy">How would it feel to be able to say, <em>“I am free to love and accept my body”</em>, and<br><em>“I am free, connected and at peace to my body”</em>?</p>
    <p class="copy">I am inviting 10 women only into this six-week healing experience, as I personally<br>know, that when we share our stories, it opens our hearts for other people to<br>share their stories. It gives us the sense we are not alone in our journey's.</p>

    <h2 class="heading">The women that come on this six-week<br>journey will receive;</h2>
    <ul class="perks">
      <li><span class="wrap">One 90mins one on one coaching session with me (which for the women that have attended the Friday circle previously, can be done before this healing circle begins);</span></li>
      <li>Private online group to continue support outside of the circle</li>
      <li>Homework outside of circle to support your healing</li>
      <li>Journal and other small gifts weekly</li>
    </ul>

    <p class="copy price">The financial investment in YOU, is <strong>$XX</strong> for the six weeks. For the women that have attended the Friday night, Gentle Bloom Sister Circle, you will receive a discount of <strong>$100</strong>, taking the price to <strong>$XX.</strong></p>

    <div class="cta">
      <div class="cta-ready">ARE YOU READY?</div>
      <div class="cta-call">Call Now</div>
      <div class="cta-phone">0491 570 156</div>
    </div>

    <div class="contact">
      <div>caroline@carolinebirchwood.com.au
        <svg width="16" height="16" viewBox="0 0 16 16" aria-hidden="true"><circle cx="8" cy="8" r="7.5" fill="var(--pink-soft)"/><rect x="4" y="5" width="8" height="6" rx="1" fill="none" stroke="#fff" stroke-width="1.2"/><path d="M4 5.5l4 3 4-3" fill="none" stroke="#fff" stroke-width="1.2"/></svg>
      </div>
      <div>carolinebirchwood.com.au
        <svg width="16" height="16" viewBox="0 0 16 16" aria-hidden="true"><circle cx="8" cy="8" r="7.5" fill="var(--pink-soft)"/><circle cx="8" cy="8" r="4" fill="none" stroke="#fff" stroke-width="1.2"/><path d="M4 8h8M8 4c-2 2.5-2 5.5 0 8M8 4c2 2.5 2 5.5 0 8" fill="none" stroke="#fff" stroke-width="1"/></svg>
      </div>
    </div>
  </section>
</main>
</body>
</html>
```